依頼詳細
依頼対象ページは「トップページ」と「アクティビティページ」になります。
※ワイヤーフレーム画像を添付いたします。参考にしてください。形状や表示位置等は必ずこの通りにしなければならないというものではありません。お任せいたします。
※利用可能なイメージを添付します。こちらもご利用下さい。

「トップページ」
・「アクティビティ画像群」は鳥沼村の観光スポットを一つずつ画像タイルにして表示させたいと考えています。
・新着情報内の画像は不要です。イメージがあればあてはめて頂いて構いません。
「アクティビティページ」
・「夏の千畳敷」と「投稿一覧」内の画像は不要です。イメージがあればあてはめて頂いて構いません。
・木曽駒ヶ岳だけでなく、その他のアクティビティページにも流用可能なデザインでお願いします。

■その他
・「トップページ」と「アクティビティページ」でヘッダーの大きさを変えて頂いても構いません
・希望色に関してオレンジまたは黒をベースを希望としています。どちらでも構いません。
・SEOを考慮したいのでデザイン内でテキストが可変となりそうな箇所はブラウザ(IE)のデフォルトフォントの使用をお願い致します。
サイトURL
http://www.vill.torinuma-ex.jp/kanko.php
ページ数
2ページ
希望イメージ
シンプル 複雑
単色 カラフル
暗い 明るい
日常 高級
遊び心 厳粛
未来的 伝統的
女性的 男性的
希望する色
オレンジベースまたは黒ベース
納品ファイル
• 高解像度JPG (.jpg)
• イラストレーター形式 (.ai)
補足説明
トップページの画像タイルは大タイル、中タイルの2種類で構成したいと考えています。
季節やイベントの有無によって入れ替えます。
タイル内の「子どもと楽しめるアイコン」「時間アイコン」「インフォメーションエリア」は
様々なアクティビティで共通で利用します。それぞれがの情報が分かりやすい形でデザインをお願いします。
遅くなりすみません。
写真素材は容量が大きいため、添付ではなく以下のURLよりダウンロードしてください。
お手数をお掛けしますが宜しくお願い致します。

■photo1
http://pakkubox-ex.jp/download/a19c3f0b72d84e6a95c1b0d7e3f28a4c6d90b1e2

■photo2
http://pakkubox-ex.jp/download/7c2e90d4b1a83f65e07d9c1b4a2f8e36d5b0c9a7

ワイヤーフレームの「アクティビティ」タイル内に入れる画像はそれぞれ該当する「もみじ谷養魚場」や「中央アルプス」などを利用してください。
全体的なイメージとして利用するものはお任せいたします。
納品ファイルですがPSD、PNG等の形式でも構いません。
お任せいたします。
素材写真の同じものを下記ミラーサイトに配置しました。
こちらからDLしても構いません。

photo1:
http://survey.kawaridojo-ex.com/photo1.zip

photo2:
http://survey.kawaridojo-ex.com/photo2.zip
・アクティビティページの「カテゴリ」に関して
→すみません。「カテゴリ名」ではなく「アクティビティ名」となります。それぞれのアクティビティを取りまとめるようなカテゴリーの概念はありません。
ミラーサイトのzipファイルが壊れていたので差し替えました。
正常にDL、解凍できることを確認しております。

ご迷惑をおかけしすみませんでした。
締切を1日延ばします。

観光協会のスタッフの皆様にサイトリニューアルのコンセプトをお伝えしたうえで、一次投票、決選投票という手順を踏んで決定いたしました。

この度は多数のご応募ありがとうございました。観光協会の方も大変喜んでおられました。

```html
<!DOCTYPE html>
<html lang="ja">
<head>
<meta charset="utf-8">
<title>信州とりぬま観光ガイド</title>
<link href="https://fonts.googleapis.com/css2?family=Noto+Sans+JP:wght@400;700&display=swap" rel="stylesheet">
<style>
:root{
  --orange:#ef8a1a;
  --orange-dark:#d9700c;
  --plum:#5b2a42;
  --bg:#ece7d8;
  --side:#ddd6bf;
  --panel:#f7f4ec;
  --ink:#3a3330;
  --muted:#7b726a;
  --lime:#a8c93a;
  --line:#cfc6ad;
  --fb:#3b5290;
}
*{box-sizing:border-box;margin:0;padding:0}
html,body{width:765px;height:1200px;overflow:hidden}
body{background:var(--bg);font-family:"Noto Sans JP",sans-serif;color:var(--ink);position:relative;font-size:10px}
.photo-strip{position:absolute;top:20px;width:56px;display:flex;flex-direction:column;gap:2px}
.photo-strip.left{left:0}
.photo-strip.right{right:0;width:51px}
.photo-strip div{height:50px}
.topbar{position:absolute;left:0;top:0;width:765px;height:20px;background:var(--panel);display:flex;justify-content:space-between;align-items:center;padding:0 12px;font-size:8px;color:var(--muted)}
.sidebar{position:absolute;left:56px;top:20px;width:118px;height:1085px;background:var(--side)}
.logo{background:var(--plum);height:82px;padding:10px;color:#fff}
.logo .name{font-size:15px;font-weight:700;line-height:1.25}
.logo .tag{font-size:7px;margin-top:6px}
.logo-sub{background:var(--plum);border-top:1px solid #7a4a60;color:#fff;font-size:7px;padding:4px 10px;white-space:nowrap}
.menu{margin:18px 8px 0;background:#fff}
.menu li{list-style:none;height:21px;display:flex;align-items:center;gap:6px;padding:0 6px;border-bottom:1px solid var(--line);font-size:8px}
.menu li::after{content:"›";margin-left:auto;color:var(--orange)}
.menu .ico{width:12px;height:12px;background:var(--orange);border-radius:2px}
.fb{margin:22px 8px 0;background:#fff;padding:6px;font-size:7px;line-height:1.4}
.fb .head{background:var(--fb);color:#fff;padding:3px 4px;font-size:7px;line-height:1.4}
.fb .body{display:flex;gap:4px;margin-top:4px;align-items:center}
.fb .sq{width:12px;height:12px;background:var(--fb);flex:none}
.faq{margin:10px 8px 0;background:var(--plum);color:#fff;font-weight:700;font-size:11px;padding:7px 8px}
.access{margin:10px 8px 0}
.access h3{font-size:7px;font-weight:400;margin-bottom:3px}
.access .map{height:92px;background:linear-gradient(135deg,#f4f1e7,#cfe0f0)}
.main{position:absolute;left:180px;top:20px;width:532px;height:1085px}
.size-ctrl{position:absolute;right:0;top:12px;display:flex;gap:3px;align-items:center;font-size:7px}
.size-ctrl span{background:var(--orange);color:#fff;padding:1px 5px;border-radius:2px}
.hero{position:absolute;left:0;top:36px;width:532px;height:215px;background:linear-gradient(160deg,#7d9b57 0%,#d36b9a 45%,#e590b8 70%,#5f7a44 100%)}
.hero h2{position:absolute;left:12px;top:14px;color:#fff;font-size:14px;font-weight:700;background:rgba(0,0,0,.25);padding:2px 8px;white-space:nowrap}
.hero .arrow{position:absolute;top:95px;width:16px;height:24px;background:rgba(0,0,0,.35)}
.hero .arrow.l{left:0}.hero .arrow.r{right:0}
.dots{position:absolute;left:250px;bottom:-12px;display:flex;gap:4px}
.dots i{width:5px;height:5px;border-radius:50%;background:#b8ae95}
.dots i:first-child{background:var(--orange)}
.tiles-big{position:absolute;left:0;top:262px;width:532px;height:200px;display:flex;gap:4px}
.tile{position:relative;background:var(--panel);border:3px solid var(--orange);overflow:hidden}
.tile .img{position:absolute;inset:0}
.tile .label{position:absolute;left:8px;bottom:8px;background:rgba(0,0,0,.55);color:#fff;font-size:11px;font-weight:700;padding:3px 7px;white-space:nowrap}
.tile .info{position:absolute;right:8px;bottom:8px;background:rgba(255,255,255,.9);font-size:7px;line-height:1.5;padding:4px 6px;width:104px;border-left:3px solid var(--orange)}
.tile .badge{position:absolute;left:8px;top:8px;width:22px;height:22px;border-radius:50%;background:var(--orange)}
.tile .clock{position:absolute;left:34px;top:8px;width:22px;height:22px;border-radius:50%;background:#fff;border:2px solid var(--orange)}
.tiles-mid{position:absolute;left:0;top:470px;width:532px;height:162px;display:flex;gap:6px}
.more{position:absolute;right:0;top:640px;background:var(--lime);color:#fff;font-size:7px;padding:2px 8px}
.news{position:absolute;left:0;top:668px;width:532px}
.news-head{display:flex;align-items:center;gap:8px;border-bottom:2px solid var(--orange);padding-bottom:4px}
.news-head h2{font-size:10px}
.news-head .sub{font-size:7px;color:var(--muted)}
.news-head .btn{background:var(--orange);color:#fff;font-size:7px;padding:1px 6px}
.item{margin-top:12px}
.item .meta{display:flex;justify-content:space-between;font-size:7px;color:var(--muted);border-bottom:1px dotted var(--line);padding-bottom:3px}
.item .meta b{background:var(--orange-dark);color:#fff;font-weight:400;padding:1px 6px}
.item .box{display:flex;gap:10px;background:var(--panel);margin:5px 0 0 4px;padding:6px;height:56px;width:310px}
.item .thumb{width:46px;height:44px;background:var(--lime);flex:none}
.item p{font-size:7px;line-height:1.5}
.contact{position:absolute;right:53px;top:1081px;background:#fff;border:1px solid var(--line);font-size:8px;padding:3px 10px}
.footer{position:absolute;left:0;top:1105px;width:765px;height:95px;background:var(--orange);color:#fff;padding:10px 0 0 100px}
.footer .fname{font-size:15px;font-weight:700}
.footer .fname small{font-size:8px;font-weight:400;margin-left:8px}
.footer address{font-style:normal;font-size:7px;line-height:1.6;margin-top:4px}
.footer .copy{position:absolute;bottom:0;left:0;width:765px;background:var(--orange-dark);text-align:center;font-size:7px;padding:4px 0}
</style>
</head>
<body>
<div class="topbar"><span>鳥沼村観光協会 / 木曽駒ヶ岳の麓の観光情報サイト</span><span>アクセス｜お問合せ｜サイトマップ</span></div>

<div class="photo-strip left">
  <div role="img" aria-label="渓流の写真" style="background:#6f8f6a"></div>
  <div role="img" aria-label="山並みの写真" style="background:#8aa6c4"></div>
  <div role="img" aria-label="花畑の写真" style="background:#b78fb0"></div>
  <div role="img" aria-label="田園の写真" style="background:#9cae6a"></div>
  <div role="img" aria-label="湖の写真" style="background:#6c8fa6"></div>
  <div role="img" aria-label="紅葉の写真" style="background:#b9743f"></div>
  <div role="img" aria-label="木立の写真" style="background:#5f7c4f"></div>
</div>
<div class="photo-strip right">
  <div role="img" aria-label="紅葉の写真" style="background:#c2532f"></div>
  <div role="img" aria-label="山頂の写真" style="background:#8aa4c0"></div>
  <div role="img" aria-label="祭りの写真" style="background:#c48a52"></div>
  <div role="img" aria-label="高原の写真" style="background:#7f9c5c"></div>
  <div role="img" aria-label="雪山の写真" style="background:#b8c8d8"></div>
  <div role="img" aria-label="新緑の写真" style="background:#6f9a58"></div>
  <div role="img" aria-label="夕景の写真" style="background:#c98a5e"></div>
</div>

<aside class="sidebar">
  <div class="logo">
    <div class="name">信州とりぬま<br>観光ガイド</div>
    <div class="tag">〜駒ヶ岳の麓 山と花の村〜</div>
  </div>
  <div class="logo-sub">鳥沼村観光協会ホームページ</div>
  <ul class="menu">
    <li><span class="ico"></span>見る</li>
    <li><span class="ico"></span>体験する</li>
    <li><span class="ico"></span>泊まる</li>
    <li><span class="ico"></span>食べる</li>
    <li><span class="ico"></span>買う</li>
  </ul>
  <div class="fb">
    <div class="head">公式ページ<br>最新情報はこちら</div>
    <div class="body"><span class="sq"></span><span>信州とりぬま<br>観光ガイド</span></div>
  </div>
  <div class="faq">よくある質問</div>
  <div class="access">
    <h3>鳥沼村への交通アクセス</h3>
    <div class="map" role="img" aria-label="鳥沼村への交通アクセス地図"></div>
  </div>
</aside>

<main class="main">
  <div class="size-ctrl">文字サイズ <span>小</span><span>中</span><span>大</span></div>
  <section class="hero" role="img" aria-label="ツツジの花と山の風景写真">
    <h2>駒見千景遺跡そばの花とアルプスのローズ</h2>
    <span class="arrow l"></span><span class="arrow r"></span>
    <div class="dots"><i></i><i></i><i></i></div>
  </section>

  <section class="tiles-big">
    <div class="tile" style="flex:1.35">
      <div class="img" role="img" aria-label="養魚場の写真" style="background:linear-gradient(150deg,#6e8b4e,#b9c98a 60%,#8a7a5a)"></div>
      <span class="badge"></span><span class="clock"></span>
      <span class="label">もみじ谷養魚場</span>
      <div class="info">営業時間 9:00〜17:00<br>定休日 毎週水曜日<br>釣りと塩焼きを楽しめます</div>
    </div>
    <div class="tile" style="flex:1">
      <div class="img" role="img" aria-label="山歩きの写真" style="background:linear-gradient(160deg,#9bb2c8,#7c9a64 70%)"></div>
      <span class="badge"></span><span class="clock"></span>
      <div class="info">所要時間 約2時間<br>初心者向けの登山道です</div>
    </div>
  </section>

  <section class="tiles-mid">
    <div class="tile" style="flex:1">
      <div class="img" role="img" aria-label="村のお祭りの写真" style="background:linear-gradient(160deg,#d9b98a,#a6784a 70%)"></div>
      <span class="badge"></span>
      <span class="label">鳥沼さわ祭り</span>
      <div class="info">開催 毎年8月<br>家族で楽しめる祭りです</div>
    </div>
    <div class="tile" style="flex:1">
      <div class="img" role="img" aria-label="木曽駒ヶ岳の山並みの写真" style="background:linear-gradient(170deg,#8fb3d6,#5e8a4e 65%,#4f6f3e)"></div>
      <span class="badge"></span>
      <span class="label">木曽駒ヶ岳</span>
      <div class="info">ロープウェイで約7分<br>中央アルプスの絶景</div>
    </div>
  </section>
  <span class="more">もっと見る</span>

  <section class="news">
    <div class="news-head"><h2>新着情報</h2><span class="sub">What's New</span><span class="btn">一覧を見る</span></div>
    <article class="item">
      <div class="meta"><span>2013/04/21　新緑散策ツアー参加者の募集について</span><b>記事を見る</b></div>
      <div class="box"><span class="thumb"></span><p>新緑散策ツアーの参加者を募集しています。春の山道をゆっくり歩きます。<br>詳しくは記事をご覧ください。</p></div>
    </article>
    <article class="item">
      <div class="meta"><span>2013/04/15　山菜採り体験の受付について</span><b>記事を見る</b></div>
      <div class="box"><span class="thumb"></span><p>山菜採り体験の受付を始めました。家族での参加も歓迎します。<br>詳しくは記事をご覧ください。</p></div>
    </article>
    <article class="item">
      <div class="meta"><span>2013/04/08　ロープウェイ運行時間のお知らせ</span><b>記事を見る</b></div>
      <div class="box"><span class="thumb"></span><p>春季のロープウェイ運行時間が変わります。お出かけ前にご確認ください。<br>詳しくは記事をご覧ください。</p></div>
    </article>
    <article class="item">
      <div class="meta"><span>2013/04/01　観光案内所の営業について</span><b>記事を見る</b></div>
      <div class="box"><span class="thumb"></span><p>観光案内所は本日より通常営業となります。お気軽にお立ち寄りください。<br>詳しくは記事をご覧ください。</p></div>
    </article>
  </section>
</main>

<span class="contact">お問い合わせ</span>

<footer class="footer">
  <div class="fname">信州とりぬま観光ガイド<small>鳥沼村観光協会</small></div>
  <address>〒399-0000 長野県上伊那郡鳥沼村1234番地　鳥沼村役場 産業振興課内<br>TEL 0265-00-1234　FAX 0265-00-5678</address>
  <div class="copy">Copyright © 2013 鳥沼村観光協会 All Rights Reserved.</div>
</footer>
</body>
</html>
```